Corbett Architecture (business card)

We need a business card design. We are a full service architectural firm that specializes in mostly residential projects and some commercial projects. We are located in Hudson Valley, New York. We work with high end clients and want a business card that is memorable and has a sleek, modern, design but will not go out of style (timeless).

Target Market(s)

high end residential clients

Industry/Entity Type

Architect

Contact Information for Business Card

Front of card
Company Logo
website: www.corbettdesignstudo.example
what we do: residential, Commercial

back of card
Owner's Name: Martin Corbett
owner's title: Principal
Business address: 2867 Orchard Lane Suite B, Maplethorpe, NY 10938
phone number: 845-555-0192
e-mail: mc@corbettdesignstudio.example

We like:
icons
sleek and clean design
simple not too busy or too much text

Font styles to use
Sans Serif

Colors
0356a4

Requirements
Must have
• company colors are navy blue, white, and gray
• Front of card
• Company Logo
• website: www.corbettdesignstudo.example
• what we do: residential, Commercial
• back of card
• Owner's Name: Martin Corbett
• owner's title: Principal
• Business address: 2867 Orchard Lane Suite B, Maplethorpe, NY 10938
• phone number: 845-555-0192
• e-mail: mc@corbettdesignstudio.example
Nice to have
• We like:
• icons
• sleek and clean design
• simple not too much text
• color of the card to be either blue or gray
Should not have
• we do not like houses in the design or plans of houses-this is over done and we don't like it.
• no QR CODES

```html
<!DOCTYPE html>
<html lang="en">
<head>
<meta charset="utf-8">
<title>Corbett Architecture – Business Card</title>
<link href="https://fonts.googleapis.com/css2?family=Open+Sans:wght@300;400;700&display=swap" rel="stylesheet">
<style>
  :root {
    --navy: #3b3a8e;
    --white: #ffffff;
    --paper: #f7f7f8;
    --gray: #8a8a90;
    --backdrop: #5e5e61;
  }
  * { margin: 0; padding: 0; box-sizing: border-box; }
  html, body {
    width: 1200px; height: 1000px; overflow: hidden;
    background: var(--backdrop);
    font-family: "Open Sans", sans-serif;
  }
  .sheet {
    width: 1200px; height: 1000px;
    display: flex; flex-direction: column;
    align-items: center; justify-content: center; gap: 70px;
  }
  .card {
    width: 560px; height: 320px;
    position: relative; overflow: hidden;
  }

  /* Front */
  .card-front {
    background: var(--navy); color: var(--white);
    display: flex; flex-direction: column; align-items: center; justify-content: center;
  }
  .front-name {
    display: flex; align-items: center; gap: 14px;
    font-weight: 400; font-size: 26px; letter-spacing: 4px; text-transform: uppercase;
  }
  .front-name .mark { width: 22px; height: 22px; background: var(--white); }
  .front-details {
    margin-top: 34px; text-align: center;
    font-size: 12px; letter-spacing: 1.5px; text-transform: uppercase; line-height: 1.7;
  }

  /* Back */
  .card-back { background: var(--paper); color: var(--navy); }
  .back-body { position: absolute; left: 44px; top: 42px; }
  .back-name {
    display: flex; align-items: center; gap: 12px;
    font-weight: 400; font-size: 22px; letter-spacing: 2px; text-transform: uppercase;
  }
  .back-name .mark { width: 18px; height: 18px; background: var(--navy); }
  .back-name small { font-size: 13px; letter-spacing: 0; text-transform: none; }
  .person { margin-top: 28px; }
  .person-name { font-weight: 700; font-size: 19px; letter-spacing: 2px; text-transform: uppercase; line-height: 1.1; }
  .person-title { font-size: 12px; letter-spacing: 2.5px; text-transform: uppercase; }
  .contacts { margin-top: 20px; list-style: none; }
  .contacts li {
    display: flex; align-items: center; gap: 10px;
    font-size: 14px; letter-spacing: 2px; text-transform: uppercase; line-height: 1.9;
  }
  .contacts svg, .address-band svg { flex: none; }
  .address-band {
    position: absolute; left: 0; right: 0; bottom: 0; height: 54px;
    background: var(--navy); color: var(--white);
    display: flex; align-items: center; gap: 10px; padding-left: 44px;
    font-size: 13px; letter-spacing: 1.5px; text-transform: uppercase;
  }
</style>
</head>
<body>
<main class="sheet">
  <section class="card card-front">
    <div class="front-name"><span class="mark"></span>Corbett Architecture</div>
    <div class="front-details">
      <p>www.corbettdesignstudo.example</p>
      <p>Residential &amp; Commercial</p>
    </div>
  </section>

  <section class="card card-back">
    <div class="back-body">
      <div class="back-name"><span class="mark"></span>Corbett Architecture <small>pllc</small></div>
      <div class="person">
        <p class="person-name">Martin Corbett</p>
        <p class="person-title">Principal</p>
      </div>
      <ul class="contacts">
        <li>
          <svg width="16" height="16" viewBox="0 0 24 24" aria-hidden="true"><path fill="currentColor" d="M6.6 10.8a15 15 0 0 0 6.6 6.6l2.2-2.2c.3-.3.7-.4 1-.2 1.1.4 2.3.6 3.6.6.6 0 1 .4 1 1V20c0 .6-.4 1-1 1A17 17 0 0 1 3 4c0-.6.4-1 1-1h3.5c.6 0 1 .4 1 1 0 1.3.2 2.5.6 3.6.1.3 0 .7-.2 1z"/></svg>
          845-555-0192
        </li>
        <li>
          <svg width="16" height="16" viewBox="0 0 24 24" aria-hidden="true"><path fill="currentColor" d="M2 5h20v14H2zm2 2v.5l8 5 8-5V7l-8 5z"/></svg>
          mc@corbettdesignstudio.example
        </li>
      </ul>
    </div>
    <div class="address-band">
      <svg width="14" height="18" viewBox="0 0 24 30" aria-hidden="true"><path fill="currentColor" d="M12 0a10 10 0 0 0-10 10c0 7.5 10 20 10 20s10-12.5 10-20A10 10 0 0 0 12 0zm0 14a4 4 0 1 1 0-8 4 4 0 0 1 0 8z"/></svg>
      2867 Orchard Lane Suite B, Maplethorpe, NY 10938
    </div>
  </section>
</main>
</body>
</html>
```